Top International Talent Management Needs creative business card design

We manage actors careers and book them liaising and promoting their profiles internationally through Casting Directors, Producers, Directors, Publicists etc. We need clearly visable contact details but with a design that reflects our status and creativity of TV, Feature Film industry. Our logo is attached and needs to relate and our website is www.quillbrookstagefolk.com
No flame designs please but please incorporate logo colours.

Target Market(s)

Clients

Industry/Entity Type

Film Production

Contact Information for Business Card

Director Rosalind Pettigrew
Suite D, Building 7, Harbourlight Lots Australia, Wren Flats, Sydney, NSW 2048

Font styles to use
Sans Serif

Colors
ec1f27

Requirements
Nice to have
• Colours should relate to logo attached and type can relate again to type in the logo design.
Should not have
• No Flames designs and best to be not too obvious with the film designs eiither. Needs to be more creative and modern

```html
<!DOCTYPE html>
<html lang="en">
<head>
<meta charset="utf-8">
<title>Quillbrook Stage Folk – Business Card</title>
<link href="https://fonts.googleapis.com/css2?family=Lato:wght@400;700&display=swap" rel="stylesheet">
<style>
  :root {
    --backdrop: #3a3330;
    --card: #121212;
    --card-edge: #1c1c1c;
    --brand-red: #ec1f27;
    --text-light: #f2f2f2;
    --text-soft: #d8d8d8;
    --divider: #2e2e2e;
    --logo-silver: #e6e6e6;
  }
  * { margin: 0; padding: 0; box-sizing: border-box; }
  html, body {
    width: 1200px;
    height: 844px;
    overflow: hidden;
    background: var(--backdrop);
    font-family: "Lato", Arial, sans-serif;
  }
  .stage {
    position: relative;
    width: 1200px;
    height: 844px;
    display: flex;
    align-items: center;
    justify-content: center;
    gap: 60px;
  }
  .card {
    position: relative;
    width: 510px;
    height: 292px;
    background: radial-gradient(ellipse at 60% 30%, var(--card-edge), var(--card) 70%);
    box-shadow: 0 14px 30px rgba(0,0,0,0.45);
    overflow: hidden;
  }
  .brand-mark {
    display: flex;
    flex-direction: column;
    align-items: flex-end;
    line-height: 1;
  }
  .brand-name {
    font-weight: 700;
    letter-spacing: 1px;
    text-transform: uppercase;
    color: var(--brand-red);
  }
  .brand-tag {
    font-weight: 400;
    color: var(--brand-red);
    margin-bottom: 3px;
  }
  .card-back .brand-mark {
    position: absolute;
    left: 34px;
    top: 150px;
  }
  .card-back .brand-name { font-size: 24px; }
  .card-back .brand-tag { font-size: 9px; }
  .divider {
    position: absolute;
    left: 262px;
    top: 40px;
    width: 1px;
    height: 190px;
    background: var(--divider);
  }
  .contact {
    position: absolute;
    left: 282px;
    top: 44px;
    color: var(--text-light);
    font-size: 14px;
    line-height: 1.3;
  }
  .contact-name {
    color: var(--brand-red);
    font-size: 19px;
    font-weight: 400;
  }
  .contact-role { font-size: 14px; margin-bottom: 16px; }
  .contact-address { color: var(--text-soft); margin-bottom: 16px; }
  .contact-line { font-size: 13px; white-space: nowrap; }
  .contact-label { color: var(--brand-red); }
  .card-front .logo-area {
    position: absolute;
    inset: 0;
    display: flex;
    align-items: center;
    justify-content: center;
  }
  .card-front .brand-name,
  .card-front .brand-tag { color: var(--logo-silver); }
  .card-front .brand-name { font-size: 38px; }
  .card-front .brand-tag { font-size: 12px; margin-bottom: 4px; }
</style>
</head>
<body>
<main class="stage">
  <section class="card card-back" aria-label="Business card, contact side">
    <div class="brand-mark">
      <span class="brand-tag">Stage Folk</span>
      <span class="brand-name">Quillbrook</span>
    </div>
    <div class="divider"></div>
    <div class="contact">
      <p class="contact-name">Rosalind Pettigrew</p>
      <p class="contact-role">Managing Director</p>
      <p class="contact-address">12345, Address Goes Here<br>Country Name, 123456.</p>
      <p class="contact-line"><span class="contact-label">T:</span> 044-987 650 312</p>
      <p class="contact-line"><span class="contact-label">E:</span> info@quillbrookstagefolk.com</p>
      <p class="contact-line"><span class="contact-label">W:</span> www.quillbrookstagefolk.com</p>
    </div>
  </section>
  <section class="card card-front" aria-label="Business card, logo side">
    <div class="logo-area">
      <div class="brand-mark">
        <span class="brand-tag">Stage Folk</span>
        <span class="brand-name">Quillbrook</span>
      </div>
    </div>
  </section>
</main>
</body>
</html>
```